office stationary for pr
pr biz stationery
Creative Brief
Simple
Adaeze Nnorom
14 mabel close eastern lagoonview estate off harmon drive lekki lagos
annorom@pelvora.com
www.pelvora.com
the logo should be used at the back of the business card

```html
<!DOCTYPE html>
<html lang="en">
<head>
<meta charset="utf-8">
<title>Pelvora Stationery Set</title>
<link href="https://fonts.googleapis.com/css2?family=Lato:wght@300;400;700&display=swap" rel="stylesheet">
<style>
  :root {
    --backdrop: #e4eef6;
    --backdrop-light: #f3f8fb;
    --paper: #ffffff;
    --ink: #6d6e71;
    --ink-soft: #9a9b9e;
    --accent: #3dbdea;
    --slate: #77787b;
    --rule: #b7b8ba;
    --shadow: rgba(60, 80, 100, 0.18);
  }
  * { box-sizing: border-box; margin: 0; padding: 0; }
  html, body { width: 1200px; height: 670px; overflow: hidden; }
  body {
    font-family: "Lato", sans-serif;
    color: var(--ink);
    background: linear-gradient(180deg, var(--backdrop-light) 0%, var(--backdrop) 100%);
    position: relative;
  }

  /* brand wordmark */
  .brand { display: inline-flex; align-items: center; gap: 4px; font-weight: 300; color: var(--ink); letter-spacing: 0.02em; }
  .brand-dot { width: 6px; height: 6px; border-radius: 50%; background: var(--accent); }
  .brand.on-colour { color: #fff; }
  .brand.on-colour .brand-dot { background: #fff; }

  /* business cards */
  .card {
    position: absolute; left: 79px; width: 161px; height: 92px;
    border-radius: 8px; background: var(--paper);
    box-shadow: 0 2px 6px var(--shadow);
    display: flex; flex-direction: column; align-items: center; justify-content: center;
  }
  .card .brand { font-size: 20px; }
  .card-front { top: 29px; justify-content: flex-start; padding-top: 8px; }
  .card-front .brand { font-size: 13px; }
  .card-front .holder { margin-top: 5px; font-size: 6px; color: var(--accent); font-weight: 700; }
  .card-front .role { font-size: 4px; color: var(--ink-soft); margin-bottom: 3px; }
  .card-front .details { font-size: 3.6px; line-height: 1.45; text-align: center; color: var(--ink-soft); width: 130px; }
  .card-blue { top: 139px; background: var(--accent); }
  .card-grey { top: 250px; background: var(--slate); }
  .card-plain { top: 360px; }

  /* letterhead */
  .letterhead {
    position: absolute; left: 269px; top: 24px; width: 341px; height: 605px;
    background: var(--paper); box-shadow: 0 2px 8px var(--shadow);
  }
  .masthead { position: absolute; left: 18px; right: 18px; top: 28px; display: flex; align-items: center; gap: 8px; }
  .masthead .rule { flex: 1; height: 1px; background: var(--rule); }
  .masthead .brand { font-size: 14px; }
  .letter-footer { position: absolute; left: 18px; bottom: 16px; font-size: 4px; line-height: 1.5; color: var(--ink-soft); width: 110px; }

  /* envelopes */
  .envelope {
    position: absolute; width: 504px; height: 244px;
    background: var(--paper); box-shadow: 0 2px 8px var(--shadow); overflow: hidden;
  }
  .envelope .flap {
    position: absolute; top: 0; right: 0; bottom: 0; width: 58px;
    display: flex; align-items: center; justify-content: center;
  }
  .flap-text { writing-mode: vertical-rl; font-size: 5px; color: #fff; letter-spacing: 0.08em; }
  .envelope .masthead { left: 16px; right: 72px; top: 30px; }
  .envelope .masthead .rule:last-child { flex: 2.2; }
  .envelope .sender { position: absolute; left: 18px; top: 118px; font-size: 4px; line-height: 1.5; color: var(--ink-soft); width: 110px; }
  .envelope-blue { left: 667px; top: 58px; }
  .envelope-blue .flap { background: var(--accent); }
  .envelope-grey { left: 667px; top: 228px; width: 480px; }
  .envelope-grey .flap { background: var(--slate); }
  .envelope-white { left: 696px; top: 384px; width: 480px; }
  .envelope-white .flap { background: #f4f5f6; border-left: 1px solid #e2e3e5; }
  .envelope-white .flap-text { color: var(--ink-soft); }
  .envelope-white .masthead { right: 20px; }
</style>
</head>
<body>

  <div class="card card-front">
    <span class="brand"><span class="brand-dot"></span>pelvora</span>
    <div class="holder">Adaeze Nnorom</div>
    <div class="role">Creative Director</div>
    <div class="details">14 mabel close eastern lagoonview estate off harmon drive lekki lagos<br>t: +234 803 555 0142<br>annorom@pelvora.com<br>www.pelvora.com</div>
  </div>
  <div class="card card-blue"><span class="brand on-colour"><span class="brand-dot"></span>pelvora</span></div>
  <div class="card card-grey"><span class="brand on-colour"><span class="brand-dot"></span>pelvora</span></div>
  <div class="card card-plain"><span class="brand"><span class="brand-dot"></span>pelvora</span></div>

  <div class="letterhead">
    <div class="masthead"><span class="rule"></span><span class="brand"><span class="brand-dot"></span>pelvora</span><span class="rule"></span></div>
    <div class="letter-footer">Pelvora<br>14 mabel close eastern lagoonview estate off harmon drive lekki lagos<br>t: +234 803 555 0142<br>annorom@pelvora.com<br>www.pelvora.com</div>
  </div>

  <div class="envelope envelope-blue">
    <div class="masthead"><span class="rule"></span><span class="brand"><span class="brand-dot"></span>pelvora</span><span class="rule"></span></div>
    <div class="sender">Pelvora<br>14 mabel close eastern lagoonview estate off harmon drive lekki lagos<br>annorom@pelvora.com</div>
    <div class="flap"><span class="flap-text">www.pelvora.com</span></div>
  </div>

  <div class="envelope envelope-grey">
    <div class="masthead"><span class="rule"></span><span class="brand"><span class="brand-dot"></span>pelvora</span><span class="rule"></span></div>
    <div class="sender">Pelvora<br>14 mabel close eastern lagoonview estate off harmon drive lekki lagos<br>annorom@pelvora.com</div>
    <div class="flap"><span class="flap-text">www.pelvora.com</span></div>
  </div>

  <div class="envelope envelope-white">
    <div class="masthead"><span class="rule"></span><span class="brand"><span class="brand-dot"></span>pelvora</span><span class="rule"></span></div>
    <div class="sender">Pelvora<br>14 mabel close eastern lagoonview estate off harmon drive lekki lagos<br>annorom@pelvora.com</div>
  </div>

</body>
</html>
```